small brochure design

I have the basic content for a brochure to describe my business services - I will need someone to take this content & elaborate and re format into something well presentable?

The logo for the business is the KVLN logo.
It should be a gold colour on black
Please feel free to change background colour and whatever you feel to make more attractive..

Looking for a small brochure 84 which is 8 printed pages including front back covers.

Can you please source & use relevant images for the topic & of my industry to use.
with content aroud the images - i.e. https://www.quarvex-find.net/results?q=stone+masonry&filter=none&agent=brw-k&hs=TpL&loc=net.quarvex:en-GB:base&origin=mnav&view=pics&sa=Z&ek=wpxhLqR2M8-4tKdjvnQZbN&vid=3XpLm_AsBqZk&w=1760&h=883

This will be used as a introduction of services –

The back inside page should be a contact page and a closing statement – I have also attached a copy of one we use that you can use as an example.

Once this is complete we will refine the content to be used in other items such as presentation folders etc … which we will get you to help create

Please contact me via email and ensure that you CC dwelt482@mailbrook.net so that my marketing manager can be across it also.

Thanks

Target Market(s)

Real Estates
Strata
Councils & Government
Herritage

Industry/Entity Type

Marketing

Requirements
Must have
• Contact Page
Examples of jobs
Lots of quality photos

```html
<!DOCTYPE html>
<html lang="en">
<head>
<meta charset="utf-8">
<title>KVLN – Trifold Brochure</title>
<link rel="stylesheet" href="https://fonts.googleapis.com/css2?family=Great+Vibes&family=Open+Sans:ital,wght@0,400;0,600;1,400&family=Tinos:ital@0;1&display=swap">
<style>
  :root {
    --page-bg: #2b2b2b;
    --black: #000000;
    --white: #ffffff;
    --gold: #bf9140;
    --brand-gold: #8a7a48;
    --rule-gold: #5e5333;
    --heading-gold: #a87a35;
    --ink: #111111;
    --stone-dark: #3b3630;
    --stone-mid: #6b625a;
    --stone-light: #8d8275;
  }
  * { box-sizing: border-box; margin: 0; padding: 0; }
  html, body { width: 1186px; height: 1200px; overflow: hidden; }
  body { background: var(--page-bg); position: relative; font-family: "Open Sans", sans-serif; }

  .brochure { position: absolute; left: 62px; top: 187px; width: 1026px; height: 798px; background: var(--black); }
  .panel { position: absolute; top: 13px; height: 770px; overflow: hidden; }

  /* Brand block: plain wordmark, rule, tagline */
  .brand { position: absolute; text-align: center; }
  .brand__name { font-family: "Open Sans", sans-serif; font-weight: 400; color: var(--brand-gold); line-height: 1; }
  .brand__rule { height: 1px; background: var(--rule-gold); margin: 8px auto 6px; }
  .brand__tagline { font-family: "Tinos", serif; color: var(--rule-gold); white-space: nowrap; }

  /* Left panel */
  .panel--packages { left: 13px; width: 321px; background: var(--white); }
  .packages__wave { position: absolute; left: 0; top: 0; }
  .packages__title { position: absolute; left: 26px; top: 4px; font-family: "Great Vibes", cursive; font-weight: 400; font-size: 46px; color: var(--ink); white-space: nowrap; }
  .packages__intro { position: absolute; left: 22px; top: 126px; width: 285px; font-size: 13px; line-height: 18.5px; color: var(--ink); }
  .packages__price { position: absolute; left: 22px; top: 226px; font-size: 30px; color: var(--ink); }
  .packages__price strong { font-weight: 600; }
  .packages__price-note { position: absolute; left: 22px; top: 264px; font-size: 16.5px; line-height: 25px; color: var(--ink); }
  .service-list { position: absolute; left: 0; width: 308px; top: 329px; text-align: center; font-family: "Tinos", serif; font-size: 22px; line-height: 35px; color: var(--heading-gold); list-style: none; }
  .packages__photo { position: absolute; left: 0; top: 436px; width: 321px; height: 334px;
    background: linear-gradient(to bottom, #e6e2dc 0%, #9b8f80 30%, #5d5348 55%, #000 80%); }
  .brand--packages { left: 0; width: 321px; top: 642px; }
  .brand--packages .brand__name { font-size: 62px; }
  .brand--packages .brand__rule { width: 242px; }
  .brand--packages .brand__tagline { font-size: 14px; }

  /* Middle panel */
  .panel--difference { left: 334px; width: 354px; background: var(--gold); }
  .difference__frame { position: absolute; left: 70px; top: 20px; width: 220px; height: 167px; background: var(--black); border-radius: 6px; }
  .difference__photo { position: absolute; left: 16px; top: 17px; width: 181px; height: 128px;
    background: linear-gradient(160deg, #cfc6b8 0%, #8a7b67 45%, #4f4536 100%); }
  .difference__title { position: absolute; left: 0; width: 354px; top: 222px; text-align: center; font-family: "Great Vibes", cursive; font-weight: 400; font-size: 40px; color: var(--white); }
  .difference__body { position: absolute; left: 37px; width: 280px; top: 286px; text-align: center; font-size: 12.8px; line-height: 18.5px; color: var(--ink); }
  .difference__body p { margin-bottom: 18.5px; }
  .difference__cta { position: absolute; left: 0; width: 354px; top: 529px; text-align: center; font-size: 20px; color: var(--white); }
  .difference__wave { position: absolute; left: 0; top: 585px; }
  .contact { position: absolute; left: 0; width: 354px; top: 643px; text-align: center; color: var(--white); }
  .contact__name { font-family: "Tinos", serif; font-size: 29px; line-height: 34px; }
  .contact__role { font-style: italic; font-size: 13px; line-height: 18px; }
  .contact__detail { font-size: 11px; line-height: 16px; }

  /* Right panel (cover) */
  .panel--cover { left: 688px; width: 328px; background: var(--black); }
  .brand--cover { left: 0; width: 328px; top: 244px; }
  .brand--cover .brand__name { font-size: 80px; }
  .brand--cover .brand__rule { width: 296px; }
  .brand--cover .brand__tagline { font-size: 16.5px; }
  .cover__photo { position: absolute; left: 2px; top: 355px; width: 324px; height: 415px;
    background: linear-gradient(to bottom, #000 0%, var(--stone-dark) 14%, var(--stone-mid) 45%, var(--stone-light) 75%, var(--stone-mid) 100%); }
  .cover__services { position: absolute; left: 0; width: 328px; top: 449px; text-align: center; list-style: none; font-family: "Tinos", serif; font-size: 23px; line-height: 49px; color: var(--white); }
  .plaque { position: absolute; left: 38px; top: 628px; width: 262px; height: 107px; background: var(--gold); text-align: center; font-family: "Tinos", serif; }
  .plaque__dot { position: absolute; width: 6px; height: 6px; border-radius: 50%; background: var(--black); }
  .plaque__name { margin-top: 8px; font-size: 23px; line-height: 26px; color: var(--ink); }
  .plaque__role { font-style: italic; font-size: 11.5px; line-height: 14px; color: var(--ink); }
  .plaque__book { margin-top: 4px; font-size: 19px; line-height: 22px; color: var(--white); }
</style>
</head>
<body>
  <main class="brochure">
    <section class="panel panel--packages">
      <svg class="packages__wave" width="321" height="110" viewBox="0 0 321 110" aria-hidden="true">
        <path d="M0 0 H321 V50 C240 30 150 72 70 72 C40 72 15 66 0 60 Z" fill="#bf9140"/>
        <path d="M0 72 C60 90 150 95 220 78 C260 68 295 64 321 66 V76 C290 74 255 80 215 90 C150 106 60 100 0 84 Z" fill="#bf9140"/>
      </svg>
      <h2 class="packages__title">Staircase packages</h2>
      <p class="packages__intro">Our staircase packages vary pending on the size and type of step and the riser. A more straight forward staircase as seen from the images below .</p>
      <p class="packages__price">Start from <strong>$300</strong></p>
      <p class="packages__price-note">for the tread and riser included .<br>Supply and install.</p>
      <ul class="service-list">
        <li>Heritage Restoration</li>
        <li>Pointin</li>
        <li>Design &amp; Construction</li>
      </ul>
      <div class="packages__photo" role="img" aria-label="Photo of a finished sandstone staircase with handrail"></div>
      <div class="brand brand--packages">
        <p class="brand__name">KVLN</p>
        <div class="brand__rule"></div>
        <p class="brand__tagline">Stone Heritage Quality Workmanship</p>
      </div>
    </section>

    <section class="panel panel--difference">
      <div class="difference__frame">
        <div class="difference__photo" role="img" aria-label="Photo of restored stone steps beside a glass balustrade"></div>
      </div>
      <h2 class="difference__title">The difference</h2>
      <div class="difference__body">
        <p>As I have showed you clearly in the photo’s above there is an outstanding difference from simply maintaining and preserving the stones natural beauty.</p>
        <p>I assure you that me and my team of stonemasons will be able to provide with uncompromising quality on all of your stone work needs.</p>
        <p>So if you think that our service may estab-lish your properties and have the potential to raise the value you can reach</p>
      </div>
      <p class="difference__cta">KVLN on : 0412 555 087</p>
      <svg class="difference__wave" width="354" height="185" viewBox="0 0 354 185" aria-hidden="true">
        <path d="M0 40 C70 0 150 0 230 18 C290 30 325 30 354 22 V185 H0 Z" fill="#000"/>
        <path d="M0 40 C70 12 150 14 230 30 C290 42 325 42 354 36 V40 C325 48 290 48 230 38 C150 22 70 22 0 46 Z" fill="#bf9140"/>
      </svg>
      <div class="contact">
        <p class="contact__name">Marco Velleri</p>
        <p class="contact__role">5th Generation Stone Mason</p>
        <p class="contact__detail">Ph:&nbsp; 0412 555 087</p>
        <p class="contact__detail">Email: marcovelleri@mailbrook.net</p>
        <p class="contact__detail">abn: 318 402 776 15</p>
      </div>
    </section>

    <section class="panel panel--cover">
      <div class="cover__photo" role="img" aria-label="Photo of a stacked natural stone feature wall"></div>
      <div class="brand brand--cover">
        <p class="brand__name">KVLN</p>
        <div class="brand__rule"></div>
        <p class="brand__tagline">Stone Heritage Quality Workmanship</p>
      </div>
      <ul class="cover__services">
        <li>Heritage Restoration</li>
        <li>Pointin</li>
        <li>Design &amp; Construction</li>
      </ul>
      <div class="plaque">
        <span class="plaque__dot" style="left:9px;top:12px"></span>
        <span class="plaque__dot" style="right:9px;top:12px"></span>
        <span class="plaque__dot" style="left:9px;bottom:12px"></span>
        <span class="plaque__dot" style="right:9px;bottom:12px"></span>
        <p class="plaque__name">Marco Velleri</p>
        <p class="plaque__role">5th Generation Stone Mason</p>
        <p class="plaque__book">Book Now<br>0412 555 087</p>
      </div>
    </section>
  </main>
</body>
</html>
```